Logo for hot realtor starting a team
The Lusk Team
Professional
Vernon Lusk III
See Attached photo
vernonlusk03@postlark.net
www.allbrackenvalehomesforsale.com
Slogan to be used - "Every Deal Closed By A Lusk"
Personal Picture and contact number
Reference draft #10 - I really like this one for a business card and I am looking for a new business card design and have a contest for this one. I will make sure to send you a request for a design. These are the changes that I would like to see and if you can make this happen, this is the winning business card, see below:
Change the style from cursive to manual script. Make the picture of what appears to be a Rose look more like a Rose. also make the font larger.
Remove the address completely and replace with my website (www.allbrackenvalehomesforsale.com and add contact number: 555-214-0386.
I would like the card to also be gray in color with black writing

```html
<!DOCTYPE html>
<html lang="en">
<head>
<meta charset="utf-8">
<title>The Lusk Team – Business Card</title>
<link rel="stylesheet" href="https://fonts.googleapis.com/css2?family=Cinzel:wght@400;700&family=Montserrat:wght@400;500&family=Great+Vibes&display=swap">
<style>
  :root {
    --backdrop: #ececec;
    --card-black: #0b0b0b;
    --brand-red: #c8202a;
    --paper-white: #ffffff;
    --ink-soft: #d9d9d9;
  }
  html, body {
    margin: 0;
    padding: 0;
    width: 1200px;
    height: 1009px;
    overflow: hidden;
    background: var(--backdrop);
  }
  .canvas {
    position: relative;
    width: 1200px;
    height: 1009px;
  }
  .card {
    position: absolute;
    width: 760px;
    height: 434px;
    border-radius: 26px;
    overflow: hidden;
    background: var(--card-black);
    box-shadow: 0 10px 24px rgba(0,0,0,0.22);
  }
  .card-back { left: 380px; top: 30px; }
  .card-front { left: 60px; top: 545px; }
  .card-shapes { position: absolute; inset: 0; }

  /* back side */
  .back-brand {
    position: absolute;
    left: 0; right: 0; top: 170px;
    text-align: center;
    font-family: "Cinzel", serif;
    font-weight: 700;
    font-size: 48px;
    letter-spacing: 3px;
    color: var(--brand-red);
  }
  .back-website {
    position: absolute;
    left: 34px; bottom: 32px;
    font-family: "Montserrat", sans-serif;
    font-size: 13px;
    letter-spacing: 4px;
    text-transform: uppercase;
    color: var(--ink-soft);
  }

  /* front side */
  .front-brand {
    position: absolute;
    left: 360px; top: 150px;
    width: 380px;
    text-align: center;
  }
  .front-brand-name {
    font-family: "Cinzel", serif;
    font-weight: 700;
    font-size: 38px;
    letter-spacing: 2px;
    color: var(--paper-white);
    line-height: 1;
    white-space: nowrap;
  }
  .front-brand-slogan {
    margin-top: 10px;
    font-family: "Great Vibes", cursive;
    font-size: 22px;
    color: var(--brand-red);
    white-space: nowrap;
  }
  .contact-list {
    position: absolute;
    left: 30px; top: 218px;
    margin: 0; padding: 0;
    list-style: none;
    font-family: "Montserrat", sans-serif;
    font-size: 14px;
    letter-spacing: 1px;
    color: var(--paper-white);
  }
  .contact-list li {
    display: flex;
    align-items: center;
    gap: 8px;
    margin-bottom: 9px;
  }
  .contact-icon { width: 12px; height: 12px; flex: none; }
  .agent-name {
    position: absolute;
    right: 40px; bottom: 24px;
    font-family: "Cinzel", serif;
    font-size: 20px;
    letter-spacing: 2px;
    color: var(--brand-red);
  }
</style>
</head>
<body>
<main class="canvas">

  <section class="card card-back" aria-label="Card back">
    <div class="back-brand">The Lusk Team</div>
    <div class="back-website">www.allbrackenvalehomesforsale.com</div>
  </section>

  <section class="card card-front" aria-label="Card front">
    <svg class="card-shapes" viewBox="0 0 760 434" width="760" height="434" aria-hidden="true">
      <path d="M0,96 C260,110 430,230 520,434" fill="none" stroke="var(--paper-white)" stroke-width="5"/>
      <path d="M0,110 C250,124 415,240 502,434" fill="none" stroke="var(--paper-white)" stroke-width="3"/>
      <path d="M0,126 C240,142 400,250 484,434 L0,434 Z" fill="var(--brand-red)"/>
      <path d="M330,434 C470,392 620,372 760,352 L760,434 Z" fill="var(--paper-white)"/>
      <path d="M330,434 C470,392 620,372 760,352" fill="none" stroke="var(--brand-red)" stroke-width="3"/>
    </svg>

    <div class="front-brand">
      <div class="front-brand-name">The Lusk Team</div>
      <div class="front-brand-slogan">Every Deal Closed By A Lusk</div>
    </div>

    <ul class="contact-list">
      <li>
        <svg class="contact-icon" viewBox="0 0 12 12"><circle cx="6" cy="6" r="6" fill="var(--paper-white)"/></svg>
        555-309-4471
      </li>
      <li>
        <svg class="contact-icon" viewBox="0 0 12 12"><circle cx="6" cy="6" r="6" fill="var(--paper-white)"/></svg>
        555-214-0386
      </li>
      <li>
        <svg class="contact-icon" viewBox="0 0 12 12"><circle cx="6" cy="6" r="6" fill="var(--paper-white)"/></svg>
        vernonlusk
      </li>
      <li>
        <svg class="contact-icon" viewBox="0 0 12 12"><circle cx="6" cy="6" r="6" fill="var(--paper-white)"/></svg>
        vernonlusk03@postlark.net
      </li>
      <li>
        <svg class="contact-icon" viewBox="0 0 12 12"><circle cx="6" cy="6" r="6" fill="var(--paper-white)"/></svg>
        www.allbrackenvalehomesforsale.com
      </li>
    </ul>

    <div class="agent-name">Vernon Lusk III</div>
  </section>

</main>
</body>
</html>
```